TalkWell needs a Letterhead

We need a letterhead for our company "TalkWell Consultants". Logo is attached. The company color is Turquoise. Icons for website, scan logo for website, icons for address, e-mail and phone appreciated rather than just words.

```html
<!DOCTYPE html>
<html lang="en">
<head>
<meta charset="utf-8">
<title>TalkWell Consultants – Letterhead</title>
<link rel="stylesheet" href="https://fonts.googleapis.com/css2?family=Ubuntu:wght@400;500&display=swap">
<style>
  :root {
    --brand-blue: #1b6fb9;
    --brand-green: #8fc024;
    --paper: #ffffff;
    --watermark: #e2e2e2;
    --backdrop: #f1f1f1;
  }
  * { box-sizing: border-box; margin: 0; padding: 0; }
  html, body {
    width: 1132px;
    height: 1200px;
    overflow: hidden;
    background: var(--backdrop);
    font-family: "Ubuntu", sans-serif;
  }
  .letterhead {
    position: relative;
    width: 1132px;
    height: 1200px;
    background: var(--paper);
  }
  .letterhead__header {
    position: absolute;
    top: 0; left: 0; right: 0;
    height: 175px;
    background: var(--paper);
    box-shadow: 0 12px 22px -8px rgba(0, 0, 0, 0.14);
    z-index: 2;
  }
  .brand {
    position: absolute;
    left: 70px;
    top: 42px;
    display: flex;
    align-items: center;
    gap: 16px;
  }
  .brand__mark {
    width: 58px;
    height: 58px;
    background: var(--brand-blue);
  }
  .brand__name {
    font-size: 32px;
    font-weight: 500;
    color: var(--brand-blue);
    line-height: 1;
  }
  .brand__tagline {
    display: block;
    margin-top: 4px;
    font-size: 11px;
    font-weight: 400;
    letter-spacing: 3.4px;
    color: var(--brand-green);
  }
  .contact {
    position: absolute;
    right: 80px;
    top: 38px;
    list-style: none;
    display: flex;
    flex-direction: column;
    gap: 9px;
  }
  .contact__item {
    display: flex;
    align-items: center;
    gap: 14px;
    font-size: 15px;
    color: var(--brand-blue);
    height: 22px;
  }
  .contact__icon {
    width: 20px;
    height: 20px;
    flex: none;
  }
  .watermark {
    position: absolute;
    left: 50%;
    top: 640px;
    width: 480px;
    height: 480px;
    transform: translate(-50%, -50%);
    border-radius: 50%;
    background: var(--watermark);
  }
  .footer-band {
    position: absolute;
    left: 0; right: 0; bottom: 0;
    height: 26px;
    display: flex;
  }
  .footer-band__segment { flex: 1; }
  .footer-band__segment--blue { background: var(--brand-blue); }
  .footer-band__segment--green { background: var(--brand-green); }
</style>
</head>
<body>
<main class="letterhead">
  <header class="letterhead__header">
    <div class="brand">
      <span class="brand__mark" aria-hidden="true"></span>
      <div class="brand__name">TalkWell<span class="brand__tagline">CONSULTANTS</span></div>
    </div>
    <ul class="contact">
      <li class="contact__item">
        <svg class="contact__icon" viewBox="0 0 20 20" aria-hidden="true"><rect x="1" y="1" width="18" height="18" rx="3" fill="var(--brand-blue)"/><path d="M7 5c-1 1-1.5 3 0 6s3.5 4.5 5.5 4.5l1-1.5-2-1.5-1 1c-1-.5-2.5-2-3-3l1-1-1.5-2z" fill="#fff"/></svg>
        <span>00 000 0000</span>
      </li>
      <li class="contact__item">
        <svg class="contact__icon" viewBox="0 0 20 20" aria-hidden="true"><path d="M10 1a6.5 6.5 0 0 0-6.5 6.5C3.5 12 10 19 10 19s6.5-7 6.5-11.5A6.5 6.5 0 0 0 10 1z" fill="var(--brand-blue)"/><circle cx="10" cy="7.5" r="2.5" fill="#fff"/></svg>
        <span>14 Quay Street</span>
      </li>
      <li class="contact__item">
        <svg class="contact__icon" viewBox="0 0 20 20" aria-hidden="true"><circle cx="10" cy="10" r="8.5" fill="none" stroke="var(--brand-blue)" stroke-width="1.8"/><ellipse cx="10" cy="10" rx="3.5" ry="8.5" fill="none" stroke="var(--brand-blue)" stroke-width="1.5"/><path d="M1.5 10h17M3 5.5h14M3 14.5h14" stroke="var(--brand-blue)" stroke-width="1.3"/></svg>
        <span>www.talkwell-example.com</span>
      </li>
      <li class="contact__item">
        <svg class="contact__icon" viewBox="0 0 20 20" aria-hidden="true"><rect x="1" y="4" width="18" height="12" fill="none" stroke="var(--brand-blue)" stroke-width="1.8"/><path d="M1.5 4.5 10 11l8.5-6.5" fill="none" stroke="var(--brand-blue)" stroke-width="1.8"/></svg>
        <span>hello@talkwell-example.com</span>
      </li>
    </ul>
  </header>

  <div class="watermark" aria-hidden="true"></div>

  <footer class="footer-band" aria-hidden="true">
    <span class="footer-band__segment footer-band__segment--blue"></span>
    <span class="footer-band__segment footer-band__segment--green"></span>
    <span class="footer-band__segment footer-band__segment--blue"></span>
    <span class="footer-band__segment footer-band__segment--green"></span>
  </footer>
</main>
</body>
</html>
```